Post Card Design Bright Lantern Youth

We need a postcard design that will be mailed to all residents offering free pickups of donated clothing. Our foundation is called Bright Lantern Youth, we are a nonprofit charitable organization that provides meals and medical services to children in need in Honduras. Collecting unwanted second-hand clothing generates revenue that helps fund the mission and programs run by our foundation. We would like to offer our pickup services to everyone who has any unwanted reusable clothing.

```html
<!DOCTYPE html>
<html lang="en">
<head>
<meta charset="utf-8">
<title>Bright Lantern Youth – Clothing Pickup Postcard</title>
<link rel="stylesheet" href="https://fonts.googleapis.com/css2?family=Roboto:wght@400;700;900&display=swap">
<style>
  :root {
    --page-bg: #ffffff;
    --card-bg: #ffffff;
    --ink: #1a1a1a;
    --headline: #ffffff;
    --accent-yellow: #ffcc00;
    --brand-green: #7dc13a;
    --rule-pink: #ec8ccb;
    --shadow: rgba(120, 95, 105, 0.55);
    --knit-light: #cfd0c8;
    --knit-rust: #9c4a1f;
    --knit-dark: #3e3a33;
    --knit-grey: #6b6c6a;
    --shirt-white: #eeeeea;
    --skin: #b88a6c;
  }
  * { box-sizing: border-box; margin: 0; padding: 0; }
  html, body {
    width: 1200px; height: 1000px; overflow: hidden;
    background: var(--page-bg);
    font-family: "Roboto", Arial, sans-serif;
    color: var(--ink);
  }
  .sheet { position: relative; width: 1200px; height: 1000px; }

  .postcard {
    position: absolute; top: 140px; width: 475px; height: 711px;
    background: var(--card-bg);
    box-shadow: 7px 6px 6px var(--shadow);
    overflow: hidden;
  }
  .postcard--front { left: 77px; }
  .postcard--back { left: 631px; }

  .side-label {
    position: absolute; top: 902px; width: 200px; text-align: center;
    font-size: 25px; font-weight: 400; letter-spacing: 0.5px;
  }
  .side-label--front { left: 214px; }
  .side-label--back { left: 768px; }

  /* Front */
  .hero-photo {
    position: absolute; left: 0; top: 0; width: 475px; height: 624px;
    background: linear-gradient(180deg,
      var(--shirt-white) 0%, #e6e5df 14%,
      var(--skin) 22%, #c9c6bb 30%,
      var(--knit-light) 42%, #a9aaa2 50%,
      var(--knit-rust) 58%, #7e3a18 70%,
      var(--knit-dark) 78%, #4a4740 86%,
      var(--knit-grey) 93%, #5a5b59 100%);
  }
  .headline {
    position: absolute; left: 47px; top: 198px;
    font-weight: 700; font-size: 58px; line-height: 59.5px;
    letter-spacing: 2px; color: var(--headline); text-transform: uppercase;
  }
  .headline .highlight { color: var(--accent-yellow); }
  .tagline {
    position: absolute; left: 47px; top: 567px;
    font-size: 19.5px; font-weight: 400; color: var(--headline);
  }
  .pickup-band { position: absolute; left: 0; top: 624px; width: 475px; height: 87px; }
  .pickup-lead {
    position: absolute; left: 48px; top: 26px;
    font-size: 14.5px; color: var(--ink);
  }
  .pickup-phone {
    position: absolute; left: 48px; top: 43px;
    font-size: 26px; font-weight: 700; letter-spacing: 1px; color: var(--brand-green);
  }

  .brand-name {
    position: absolute; text-align: center;
    font-weight: 700; color: var(--brand-green);
  }
  .brand-name .brand-dot {
    display: block; margin: 0 auto 5px; border-radius: 50%; background: var(--brand-green);
  }
  .pickup-band .brand-name { left: 382px; top: 14px; width: 74px; font-size: 12px; line-height: 13px; }
  .pickup-band .brand-dot { width: 20px; height: 20px; }

  /* Back */
  .writing-lines { position: absolute; left: 15px; top: 0; width: 443px; height: 620px; }
  .about {
    position: absolute; left: 26px; top: 641px; width: 320px;
    font-size: 9.6px; line-height: 10px; text-align: justify; color: var(--brand-green);
  }
  .postcard--back .brand-name { left: 360px; top: 622px; width: 92px; font-size: 14px; line-height: 15px; }
  .postcard--back .brand-dot { width: 28px; height: 28px; }
</style>
</head>
<body>
<main class="sheet">

  <section class="postcard postcard--front" aria-label="Postcard front">
    <div class="hero-photo" role="img" aria-label="Photo of a hand resting on a stack of folded knit sweaters in cream, rust, charcoal and grey"></div>
    <h1 class="headline">Your<br>Unwanted<br>Clothes<br>Can Create<br>A <span class="highlight">Brighter</span><br>Future!</h1>
    <p class="tagline">Donate Today, Change a Child’s Tomorrow!</p>
    <div class="pickup-band">
      <p class="pickup-lead">Arrange Your Free Pickup – It’s Quick and Easy!</p>
      <p class="pickup-phone">CALL: (555) 014-2287</p>
      <div class="brand-name"><span class="brand-dot"></span>Bright Lantern Youth</div>
    </div>
  </section>

  <section class="postcard postcard--back" aria-label="Postcard back">
    <svg class="writing-lines" viewBox="0 0 443 620" aria-hidden="true">
      <g stroke="var(--rule-pink)" stroke-width="0.8">
        <line x1="0" y1="497" x2="443" y2="497"/>
        <line x1="0" y1="514" x2="443" y2="514"/>
        <line x1="0" y1="533" x2="443" y2="533"/>
        <line x1="0" y1="551" x2="443" y2="551"/>
        <line x1="0" y1="569" x2="443" y2="569"/>
        <line x1="0" y1="588" x2="443" y2="588"/>
        <line x1="0" y1="608" x2="443" y2="608"/>
      </g>
    </svg>
    <p class="about">We are a nonprofit charitable organization that provides meals and medical services to children in need in Honduras. Collecting unwanted second-hand clothing generates revenue that helps fund the mission and programs run by our foundation. We would like to offer our pickup services to everyone who has any unwanted reusable clothing.</p>
    <div class="brand-name"><span class="brand-dot"></span>Bright Lantern Youth</div>
  </section>

  <p class="side-label side-label--front">FRONT</p>
  <p class="side-label side-label--back">BACK</p>

</main>
</body>
</html>
```